Medien Firma benötigt Briefpapier
Zielgruppe
Firma:
Wir sind im Bereich Veranstaltungstechnik und Eventmanagement seit 2007 tätig. Ab 2009 konnten wir unsere Expertise um die Bereiche Medientechnik und TV Produktion erweitern. Durch dieses Portfolio sind wir in der Lage, alle Facetten der technischen Planung durchzuführen.
Bereiche:
Veranstaltungstechnik - Medientechnik - Livestreaming
Kunden:
B2B
Aufgabenstellung
Erstellung von Briefpapier mit dem vorhandenen Logo.
Das Briefpapier soll auch als Produktsheet nutzbar sein. Also muss der Footer Text austauschbar sein.
Schlicht, Modern, Zeitlos, max. zwei Farben

```html
<!DOCTYPE html>
<html lang="de">
<head>
<meta charset="utf-8">
<title>lumenfield – Briefpapier und Produktsheet</title>
<link rel="stylesheet" href="https://fonts.googleapis.com/css2?family=Ubuntu:wght@300;400&family=Raleway:wght@400;600&display=swap">
<style>
  :root {
    --stage: #97a8af;
    --paper: #ffffff;
    --brand-blue: #009fe0;
    --tint-blue: #e2f3fa;
    --rule-blue: #a9dcf2;
    --ink: #1c1c1c;
  }
  html, body {
    margin: 0;
    width: 1200px;
    height: 960px;
    overflow: hidden;
    background: var(--stage);
  }
  .sheet {
    position: absolute;
    top: 101px;
    width: 536px;
    height: 758px;
    background: var(--paper);
    box-shadow: 0 10px 30px rgba(40, 55, 62, 0.45);
  }
  .sheet svg { display: block; width: 100%; height: 100%; }
  .sheet--letterhead { left: 29px; }
  .sheet--cover { left: 632px; }

  .tint-wedge { fill: var(--tint-blue); }
  .cover-field { fill: var(--brand-blue); }
  .cover-wedge { fill: var(--paper); }

  .wordmark {
    font-family: "Ubuntu", sans-serif;
    font-weight: 300;
    fill: var(--ink);
  }
  .wordmark-dot { fill: none; stroke: var(--ink); }

  .sender-name {
    font-family: "Raleway", sans-serif;
    font-weight: 600;
    font-size: 5.4px;
    fill: var(--brand-blue);
  }
  .sender-line, .footer-line {
    font-family: "Raleway", sans-serif;
    font-weight: 400;
    font-size: 5.4px;
    fill: var(--ink);
  }
  .footer-link { fill: var(--brand-blue); }
  .footer-rule { stroke: var(--rule-blue); stroke-width: 1; }
</style>
</head>
<body>

<div class="sheet sheet--letterhead">
  <svg viewBox="0 0 536 758" aria-label="Briefpapier lumenfield">
    <polygon class="tint-wedge" points="0,0 450,379 0,758"/>

    <g class="wordmark-group">
      <circle class="wordmark-dot" cx="362" cy="106" r="8.5" stroke-width="1.2"/>
      <text class="wordmark" x="511" y="113" font-size="21" text-anchor="end">lumenfield</text>
    </g>

    <text class="sender-name" x="63" y="119">lumenfield</text>
    <text class="sender-line" x="63" y="128">Musterstraße 1 | 12345 Musterstadt | info@lumenfield.de</text>

    <line class="footer-rule" x1="63" y1="671" x2="473" y2="671"/>
    <text class="footer-line" x="63" y="689">Musterstraße 1, 12345 Musterstadt | Tel. 0123 456 789 | info@lumenfield.de | <tspan class="footer-link">www.lumenfield.de</tspan></text>
    <text class="footer-line" x="63" y="702">Finanzamt Musterstadt | Ust.ID: DE 123 456 789 | BV: Musterbank | BIC: ABCDEFGHI | IBAN: DE 1234 5678 9012 3456 7890</text>
  </svg>
</div>

<div class="sheet sheet--cover">
  <svg viewBox="0 0 536 758" aria-label="Produktsheet Deckblatt lumenfield">
    <rect class="cover-field" x="0" y="0" width="536" height="758"/>
    <polygon class="cover-wedge" points="0,0 451,379 0,758"/>

    <g class="wordmark-group">
      <circle class="wordmark-dot" cx="52" cy="379" r="13" stroke-width="1.6"/>
      <text class="wordmark" x="72" y="391" font-size="34">lumenfield</text>
    </g>
  </svg>
</div>

</body>
</html>
```